Business Card Design Falcon Ridge Autos

Used car dealership, We buy, sell, trade and finance a cars.

Industry/Entity Type

Finance

Contact Information for Business Card

Falcon Ridge Autos, Buy, Sell, Trade, Finance, 418 Larkspur Ave, Bramblewick, ME, 04837, 555-318-6092, www.Falcon-Ridge-Autos.example

Requirements
Must have
• Crown
Nice to have
• purple and gold colors

```html
<!DOCTYPE html>
<html lang="en">
<head>
<meta charset="utf-8">
<title>Falcon Ridge Autos – Business Card</title>
<link rel="stylesheet" href="https://fonts.googleapis.com/css2?family=Roboto:wght@400;700;900&display=swap">
<style>
  :root {
    --purple: #3c1a8c;
    --purple-deep: #2e1170;
    --gold: #f2c21b;
    --gold-soft: #d9b13a;
    --white: #ffffff;
    --backdrop: #cdcac5;
  }
  * { margin: 0; padding: 0; box-sizing: border-box; }
  html, body { width: 1200px; height: 800px; overflow: hidden; }
  body {
    background: var(--backdrop);
    display: flex; align-items: center; justify-content: center;
    font-family: "Roboto", Arial, sans-serif;
  }
  .card {
    position: relative;
    width: 840px; height: 480px;
    background: var(--white);
    overflow: hidden;
  }
  .card__top-stripe {
    position: absolute; left: 0; top: 0; width: 100%; height: 18px;
    background: var(--purple);
  }
  .brand {
    position: absolute; left: 0; top: 62px; width: 100%;
    text-align: center;
  }
  .brand__name {
    display: inline-flex; align-items: center; gap: 16px;
    font-weight: 900; font-size: 62px; line-height: 1;
    color: var(--purple); text-transform: uppercase; letter-spacing: -1px;
  }
  .brand__dot {
    width: 18px; height: 18px; border-radius: 50%; background: var(--gold);
  }
  .brand__tagline {
    margin-top: 22px;
    font-weight: 700; font-size: 30px; letter-spacing: 2px;
    color: var(--purple);
  }
  .card__rule {
    position: absolute; left: 0; top: 220px; width: 100%; height: 4px;
    background: var(--purple);
  }
  .card__band {
    position: absolute; left: 0; top: 232px; width: 100%; bottom: 0;
    background: linear-gradient(180deg, var(--purple) 0%, var(--purple-deep) 100%);
  }
  .person {
    position: absolute; left: 64px; top: 40px;
    color: var(--gold);
  }
  .person__name { font-size: 24px; line-height: 1.1; }
  .person__name strong { font-weight: 700; }
  .person__role {
    margin-top: 6px; margin-left: 40px;
    font-size: 12px; letter-spacing: 1px; color: var(--gold-soft);
  }
  .divider {
    position: absolute; left: 410px; top: 40px; width: 2px; height: 160px;
    background: var(--purple-deep); box-shadow: 1px 0 0 rgba(255,255,255,.08);
  }
  .contact {
    position: absolute; left: 440px; top: 60px; right: 24px;
    list-style: none; color: var(--white); font-size: 16px; line-height: 1.2;
  }
  .contact__item { display: flex; align-items: center; gap: 12px; margin-bottom: 18px; white-space: nowrap; }
  .contact__item--phone { color: var(--gold); font-weight: 700; }
  .contact__icon { width: 18px; height: 18px; flex: none; }
</style>
</head>
<body>
  <article class="card">
    <div class="card__top-stripe"></div>
    <header class="brand">
      <div class="brand__name"><span class="brand__dot"></span>Falcon Ridge Autos</div>
      <p class="brand__tagline">BUY, SELL, TRADE, FINANCE</p>
    </header>
    <div class="card__rule"></div>
    <section class="card__band">
      <div class="person">
        <p class="person__name"><strong>NAME</strong> SURNAME</p>
        <p class="person__role">DESIGNATION</p>
      </div>
      <div class="divider"></div>
      <ul class="contact">
        <li class="contact__item">
          <svg class="contact__icon" viewBox="0 0 24 24"><path fill="#fff" d="M12 2a7 7 0 0 0-7 7c0 5 7 13 7 13s7-8 7-13a7 7 0 0 0-7-7zm0 9.5A2.5 2.5 0 1 1 12 6.5a2.5 2.5 0 0 1 0 5z"/></svg>
          418 Larkspur Ave, Bramblewick, ME, 04837
        </li>
        <li class="contact__item contact__item--phone">
          <svg class="contact__icon" viewBox="0 0 24 24"><path fill="#f2c21b" d="M6.6 10.8a15 15 0 0 0 6.6 6.6l2.2-2.2a1 1 0 0 1 1-.25 11.4 11.4 0 0 0 3.6.57 1 1 0 0 1 1 1V20a1 1 0 0 1-1 1A17 17 0 0 1 3 4a1 1 0 0 1 1-1h3.5a1 1 0 0 1 1 1c0 1.25.2 2.45.57 3.6a1 1 0 0 1-.25 1z"/></svg>
          555-318-6092
        </li>
        <li class="contact__item">
          <svg class="contact__icon" viewBox="0 0 24 24"><g fill="none" stroke="#fff" stroke-width="2"><circle cx="12" cy="12" r="9"/><path d="M3 12h18M12 3c3 3.5 3 14.5 0 18M12 3c-3 3.5-3 14.5 0 18"/></g></svg>
          www.Falcon-Ridge-Autos.example
        </li>
      </ul>
    </section>
  </article>
</body>
</html>
```